Tobin's Jewelry Studio Needs a Moving Location Flyer

We need a flyer to inform our customers of our location moving. We will be moving to our city's downtown which is only 1 mile away from our current address. We will be having a moving sale ( Up to 80% off). The sale starts Sept. 8th Our business creates, sells, and repairs fine jewelry. Dimensions are 5"x8"

Target Market(s)

Women ages 25-55

Industry/Entity Type

Jewelry

Colors
85abd2
cfdeed

Requirements
Must have
• Our logo
• Mention of the sale
• Our current address
• 4785 Cresthaven Blvd.
• Dunmore, Ca 94318
• (415)826-3319
Nice to have
• Mention that we're relocating to downtown Dunmore (new location opening Nov. 1st.)

```html
<!DOCTYPE html>
<html lang="en">
<head>
<meta charset="utf-8">
<title>Tobin's Jewelry Studio — Moving Sale Flyer</title>
<link rel="stylesheet" href="https://fonts.googleapis.com/css2?family=Gelasio:wght@400;700&family=Comfortaa:wght@300&display=swap">
<style>
  :root {
    --page-bg: #e4e4e2;
    --paper: #ffffff;
    --navy: #1d3f63;
    --band-deep: #4d7a9a;
    --band-mid: #85abd2;
    --band-pale: #cfdeed;
    --muted: #6f8296;
    --logo-blue: #a9d6e2;
    --address: #8fb3c7;
    --white: #ffffff;
  }
  * { margin: 0; padding: 0; box-sizing: border-box; }
  html, body { width: 1200px; height: 1200px; overflow: hidden; }
  body { background: var(--page-bg); position: relative; font-family: "Gelasio", Georgia, serif; }

  .flyer {
    position: absolute; left: 260px; top: 56px;
    width: 680px; height: 1088px;
    background: var(--paper);
    overflow: hidden;
    box-shadow: 0 6px 24px rgba(0,0,0,0.12);
  }
  .sale-band {
    position: absolute; left: 0; right: 0; top: 330px; height: 600px;
    background: linear-gradient(180deg,
      var(--paper) 0%,
      var(--band-pale) 10%,
      var(--band-mid) 24%,
      var(--band-deep) 42%,
      var(--band-deep) 70%,
      var(--band-mid) 84%,
      var(--band-pale) 92%,
      var(--paper) 100%);
  }
  .photo-ring {
    position: absolute; left: 50px; top: 90px; width: 190px; height: 170px;
    border-radius: 50%;
    background: radial-gradient(circle at 45% 45%, #c9dcef 0%, #6c93c4 45%, #d8dde3 75%, rgba(255,255,255,0) 100%);
  }
  .photo-necklace {
    position: absolute; left: 300px; top: 20px; width: 360px; height: 320px;
    border-radius: 40% 40% 50% 50%;
    background: radial-gradient(circle at 50% 45%, #c4323a 0%, #b8463c 35%, #7aa0a0 65%, rgba(255,255,255,0) 100%);
  }
  .headline {
    position: absolute; left: 44px; top: 366px;
    font-weight: 700; font-size: 42px; line-height: 44px;
    color: var(--navy);
  }
  .discount-figure {
    position: absolute; left: 0; top: 0; width: 680px; height: 1088px;
    pointer-events: none;
  }
  .discount-figure text {
    font-family: "Comfortaa", "Trebuchet MS", sans-serif; font-weight: 300;
    font-size: 340px; fill: var(--white);
  }
  .discount-percent {
    position: absolute; left: 592px; top: 536px;
    font-size: 62px; line-height: 1; color: var(--white);
  }
  .discount-off {
    position: absolute; left: 592px; top: 606px;
    font-size: 44px; line-height: 1; color: var(--white);
  }
  .discount-lead {
    position: absolute; left: 40px; top: 770px;
    font-size: 36px; line-height: 1; color: var(--white);
  }
  .sale-name {
    position: absolute; left: 190px; top: 838px;
    font-weight: 700; font-size: 46px; line-height: 1; color: var(--navy); white-space: nowrap;
  }
  .sale-date {
    position: absolute; left: 262px; top: 896px;
    font-size: 28px; line-height: 1; color: var(--muted); white-space: nowrap;
  }
  .studio-name {
    position: absolute; left: 0; right: 0; top: 950px;
    display: flex; align-items: center; justify-content: center; gap: 12px;
    font-size: 24px; line-height: 1; color: var(--navy);
  }
  .studio-dot { width: 28px; height: 28px; border-radius: 50%; background: var(--logo-blue); }
  .address {
    position: absolute; left: 0; right: 0; top: 1000px; text-align: center;
    font-size: 17px; line-height: 1; letter-spacing: 3px; color: var(--address);
  }
  .phone {
    position: absolute; left: 0; right: 0; top: 1030px; text-align: center;
    font-size: 17px; line-height: 1; letter-spacing: 3px; color: var(--address);
  }
</style>
</head>
<body>
  <main class="flyer">
    <div class="sale-band"></div>
    <div class="photo-ring" role="img" aria-label="Photo of a silver ring set with three blue and pavé stones"></div>
    <div class="photo-necklace" role="img" aria-label="Photo of a colourful beaded statement necklace in red, green and blue"></div>

    <h1 class="headline">November 1st<br>we’re heading<br>downtown</h1>

    <svg class="discount-figure" viewBox="0 0 680 1088" aria-label="80">
      <text x="150" y="818" textLength="430" lengthAdjust="spacingAndGlyphs">80</text>
    </svg>
    <div class="discount-lead">up to</div>
    <div class="discount-percent">%</div>
    <div class="discount-off">off</div>

    <p class="sale-name">in our moving sale</p>
    <p class="sale-date">from September 8th</p>

    <div class="studio-name"><span class="studio-dot"></span>Tobin's Jewelry Studio</div>
    <p class="address">4785 Cresthaven Blvd., Dunmore, Ca 94318</p>
    <p class="phone">(415)826-3319</p>
  </main>
</body>
</html>
```